TalkLoom Website Re-skin

TalkLoom.com needs to be re-skinned. The form design of the website and talkloom logo are is to stay as-is. The images, type font and background color need to be updated to attempt to achieve a professionally-progressive first impression. We are also amiable to any recommended copy changes, but the main focus of this initiative is to replace the tired and muted existing images, background, and type font. I have included a number of websites that have the look and feel that we would like to inspire the refresh.... These websites also do a good job to include images that blend a computer, slatepad, or zenphone with a somewhat blurred background.

I included two company overview documents to describe the service. You can also log into the site and receive 5 Free interviews so that you can experience the site yourself in about 10 minutes.

Another high level overview is described in this video link:
http://clipnest.example/q7Rt-2Kxm
Updates

We received some questions from a few designers and I want to make sure that I share my responses with everyone.  

How many pages do we want:  
We would like 3 pages.  The Home Page, the Login Page, and the Create Account Page.  Note: The large majority of the work should be focused on the Home Page.  The Login and Create Account pages just need to have the background and overall theme from the Home Page design.  

Is coding a must for the Project:  
Coding is highly preferred as it will help reduce the process of splicing up the artwork files.  As such, our preference is to obtain the coding with the project. 

What type of Coding do we want?
HTML/CSS is acceptable

Note:  I also added some Logo .png files onto the sketch harbor site

Target Market(s)

Please refer to the attached "company description" and "business overview" documents. General target audience is small, medium and large organizations seeking to reduce the time and cost to interview qualified job candidates. Given that TalkLoom serves small to large organizations, we would like our design to error on the size of "professionally progressive" such that it has the visual appearance of being sophisticated and technologically sound.

Industry/Entity Type

Computer

Requirements
Must have
• Seeking to have 3 pages re-skinned. The Home Page, the Login Page, and the Create Account Page. Note. The Login and Create Account Pages should be very straight forward with limited work required as we seek little design change for them and would like them to carry over the theme and colors from the Home Page. Hence, re-skinning the home page with the elements described below is the major focus.

Top of Home Page: Replace main image of lady coming out of resume/slatepad screen with an image very similar to the one on the attached file titled "plimbo home page lady" Note: Plimbo changed its name to Tavrix so duplicating this approach is okay to mimic this image without issue. We especially like this image as it is colorful and visually describes the service we provide.

The layout of the "Orv SlatePad" and "Dolvex Home page slate-pad" files that are attached are nice. There may be a way to leverage the plimbo lady with the Orv Slatepad image to make a nice visual.

Verbiage: Change copy from "Welcome to Talkloom! Talkloom is your fully automated interviewing solution. Personalized to your brand, you will save time and money selecting the best candidates" To Now Read: "Humanize and accelerate your interview screening process with TalkLoom."

Background: We really like the way that Orv changes their back-grounds as the themes/subjects change when scrolling down their main web page. Achieving this sort of experience would be ideal. It is also acceptable to have a more contrasting background color that may be darker. If this is done, then the words could be in white. This is not a requirement, just some general direction.

Font type: We like the font type from Orv (see attached file titled "Orv SlatePad")

Font Color: Okay to change font from the dull blue that we have today and use a different more contrasting or popping color.

We like outlining steps 1 through 4 but prefer to replace the people holding the placards with some other images that are potentially in a family of images that all tie together.

It is okay to keep the images in the "Responsive Layout" section of the site (located about 3/4ths of the way down the page) as these seem to be more current and do a good job to illustrate images with an slatepad or computer.

Benefits Section: Prefer to change this section. Listing nine (9) separate benefits are too many to make any impact. Advocate illustrating the following benefits:
- "Reduce time and cost to screen candidates"
- "Design site with your logo and colors"
- "Customize interview questions for all your postings"
- "Interview candidates anywhere in the world"
- "Review candidate video's anytime / anywhere"

Nice to have
• Potential to add an image whereby it shows / illustrates talkloom's administrative portal "talkloom admin portal" (attached) to an image of an slatepad screen similar to how the attached images for the following websites: "Dolvex" "WeareHollyfen" and "brambleway"

```html
<!DOCTYPE html>
<html lang="en">
<head>
<meta charset="utf-8">
<title>TalkLoom – Login</title>
<link href="https://fonts.googleapis.com/css2?family=Roboto:ital,wght@0,300;0,400;1,300;1,400&display=swap" rel="stylesheet">
<style>
  :root {
    --brand-navy: #1a5e9c;
    --brand-navy-dark: #154f86;
    --footer-sky: #0aa3e3;
    --title-blue: #1f5f9b;
    --link-blue: #2a8fc4;
    --nav-grey-top: #fbfbfb;
    --nav-grey-bottom: #dcdcde;
    --field-border: #dcdcdc;
    --placeholder: #a8a8a8;
    --muted: #8c8c8c;
    --white: #ffffff;
    --ink: #333333;
  }
  * { box-sizing: border-box; margin: 0; padding: 0; }
  html, body { width: 1200px; height: 660px; overflow: hidden; background: var(--white); }
  body { position: relative; font-family: "Roboto", Arial, sans-serif; color: var(--ink); }

  .site-header { position: absolute; left: 0; top: 0; width: 1200px; height: 97px; background: var(--brand-navy); }
  .brand { position: absolute; left: 104px; top: 10px; display: flex; align-items: center; gap: 10px; }
  .brand-dot { width: 66px; height: 66px; border-radius: 50%; background: #3aa9e6; }
  .brand-name { font-size: 24px; font-weight: 400; color: var(--white); letter-spacing: 0.5px; }

  .header-actions { position: absolute; top: 36px; left: 833px; display: flex; gap: 10px; }
  .header-btn {
    height: 28px; padding: 0; border-radius: 4px; font-size: 15px; color: #222; white-space: nowrap;
    background: linear-gradient(#ffffff, #d9d9d9); border: 1px solid #c8c8c8;
    display: flex; align-items: center; justify-content: center;
  }
  .header-btn.login { width: 80px; }
  .header-btn.create { width: 122px; }

  .main-nav { position: absolute; left: 0; top: 97px; width: 1200px; height: 45px;
    background: linear-gradient(var(--nav-grey-top), var(--nav-grey-bottom)); }
  .nav-item { position: absolute; top: 0; height: 45px; display: flex; align-items: center; font-size: 15px; color: #666; white-space: nowrap; }
  .nav-item.active { left: 101px; width: 94px; justify-content: center; background: var(--brand-navy); color: var(--white); }
  .nav-item.pricing { left: 207px; }

  .login-title { position: absolute; top: 177px; left: 0; width: 1180px; text-align: center; white-space: nowrap;
    font-size: 32px; font-weight: 300; color: var(--title-blue); }

  .field { position: absolute; left: 415px; width: 364px; height: 42px; border: 1px solid var(--field-border);
    border-radius: 10px; padding-left: 14px; display: flex; align-items: center;
    font-size: 16px; font-weight: 300; font-style: italic; color: var(--placeholder); background: var(--white); }
  .field.username { top: 243px; }
  .field.password { top: 296px; font-size: 13px; letter-spacing: 1px; }

  .forgot-link { position: absolute; left: 422px; top: 358px; font-size: 14px; font-weight: 300; font-style: italic; color: var(--link-blue); white-space: nowrap; }
  .remember { position: absolute; left: 659px; top: 359px; display: flex; align-items: center; gap: 9px; white-space: nowrap;
    font-size: 12px; font-style: italic; font-weight: 300; color: var(--muted); }
  .checkbox { width: 16px; height: 16px; border: 1px solid #cfcfcf; border-radius: 4px; background: linear-gradient(#fff, #ececec); }

  .submit-btn { position: absolute; left: 695px; top: 399px; width: 77px; height: 45px; background: var(--brand-navy);
    color: var(--white); font-size: 18px; font-weight: 300; display: flex; align-items: center; justify-content: center; }

  .site-footer { position: absolute; left: 0; top: 503px; width: 1200px; height: 157px; background: var(--footer-sky); color: var(--white); }
  .footer-heading { font-size: 15px; font-weight: 400; white-space: nowrap; }
  .value-col { position: absolute; left: 108px; top: 20px; width: 455px; }
  .value-col p { margin-top: 10px; font-size: 14.5px; font-weight: 300; line-height: 24px; }
  .divider { position: absolute; top: 28px; width: 2px; height: 117px; background: var(--white); }
  .divider.first { left: 588px; }
  .divider.second { left: 793px; }
  .contact-col { position: absolute; left: 616px; top: 20px; }
  .contact-col ul { list-style: none; margin-top: 10px; padding-left: 3px; font-size: 14.5px; font-weight: 300; line-height: 24px; white-space: nowrap; }
  .follow-col { position: absolute; left: 960px; top: 20px; width: 136px; text-align: center; }
  .social-row { margin-top: 13px; display: flex; justify-content: center; gap: 7px; }
  .social-square { width: 25px; height: 25px; border-radius: 2px; background: var(--brand-navy-dark); }
</style>
</head>
<body>
  <header class="site-header">
    <div class="brand">
      <span class="brand-dot"></span>
      <span class="brand-name">TalkLoom</span>
    </div>
    <div class="header-actions">
      <span class="header-btn login">Login</span>
      <span class="header-btn create">Create Account</span>
    </div>
  </header>

  <nav class="main-nav">
    <span class="nav-item active">Benefits</span>
    <span class="nav-item pricing">Pricing</span>
  </nav>

  <main>
    <h1 class="login-title">Login To Your Account</h1>
    <div class="field username">Username</div>
    <div class="field password">******</div>
    <span class="forgot-link">Forgot your password ?</span>
    <label class="remember"><span class="checkbox"></span>Remember me</label>
    <span class="submit-btn">Login</span>
  </main>

  <footer class="site-footer">
    <section class="value-col">
      <h2 class="footer-heading">The TalkLoom Value</h2>
      <p>TalkLoom video interviewing makes prescreening potential employees quick, safe, and extremely easy. With no contracts, hidden fees, or complicated user interfaces, we make video screening / interviewing a snap.</p>
    </section>
    <span class="divider first"></span>
    <section class="contact-col">
      <h2 class="footer-heading">Contact Us</h2>
      <ul>
        <li>E | info@talkloom.com</li>
        <li>Privacy Policy</li>
        <li>Terms and Conditions</li>
      </ul>
    </section>
    <span class="divider second"></span>
    <section class="follow-col">
      <h2 class="footer-heading">Follow us on</h2>
      <div class="social-row">
        <span class="social-square" role="img" aria-label="Social profile link"></span>
        <span class="social-square" role="img" aria-label="Social profile link"></span>
        <span class="social-square" role="img" aria-label="Social profile link"></span>
      </div>
    </section>
  </footer>
</body>
</html>
```